We need an eye catching logo design and Business Card that portrays our business, which is the cleaning and protecting of stainless steel with an organic non chemical product. This can be separate to the company name or can incorporate it. Maybe even just the company name itself. Company Name is Gleamwise Gleamwise.
Ideal for products exposed to weather elements, ie: balustrading, enclosures, BBQs, we also supply the product so you can do it yourself (DIY).
In addition we would want to include on this card:
1. My Name (Paul Dremmick)
2. Mobile No. (TBA Later)
3. Email address (TBA Later)
4. Web address (TBA Later)
Updates

Please note that we also need suggestions on a logo, as this we do not have this either.

Please note we have update our brief to be more specific.

Thank You.

Paul

Reason: Awaiting for a couple of revised submissions from feedback given.

Target Market(s)

Purchasing officers and government people.

Industry/Entity Type

Steel

Colors

Designer to choose colors to be used in the design.

Requirements
Must have
• 1. Name (Paul Dremmick)
2. Mobile No. (TBA Later)
Should not have
• Should not be to busy looking

```html
<!DOCTYPE html>
<html lang="en">
<head>
<meta charset="utf-8">
<title>Gleamwise Gleamwise – Business Card</title>
<link rel="stylesheet" href="https://fonts.googleapis.com/css2?family=Michroma&family=Exo+2:ital,wght@1,400&family=Questrial&family=Open+Sans:wght@400&display=swap">
<style>
  :root {
    --paper: #ffffff;
    --steel-dark: #1c1d1f;
    --steel-mid: #2e3033;
    --steel-light: #45484c;
    --band-light: #6a6d70;
    --band-dark: #3a3c3f;
    --gold: #c9b27a;
    --text: #ffffff;
    --text-soft: #e4e4e4;
    --rule: rgba(255,255,255,0.22);
  }
  * { box-sizing: border-box; margin: 0; padding: 0; }
  html, body {
    width: 1046px; height: 1200px; overflow: hidden;
    background: var(--paper);
  }
  .sheet { position: relative; width: 1046px; height: 1200px; }

  .card {
    position: absolute; left: 0; width: 1046px; overflow: hidden;
    background:
      repeating-linear-gradient(180deg, rgba(255,255,255,0.025) 0 1px, rgba(0,0,0,0.04) 1px 3px, rgba(255,255,255,0.015) 3px 4px),
      radial-gradient(ellipse 70% 60% at 50% 30%, var(--steel-light) 0%, var(--steel-mid) 45%, var(--steel-dark) 100%);
  }
  .card--front { top: 0; height: 574px; }
  .card--back { top: 620px; height: 580px; }

  /* Front */
  .brand-band {
    position: absolute; left: 0; top: 222px; width: 1046px; height: 109px;
    background:
      repeating-linear-gradient(180deg, rgba(255,255,255,0.04) 0 1px, rgba(0,0,0,0.05) 1px 3px),
      linear-gradient(90deg, var(--band-dark) 0%, var(--band-light) 50%, var(--band-dark) 100%);
    border-top: 1px solid rgba(255,255,255,0.18);
    border-bottom: 1px solid rgba(0,0,0,0.6);
  }
  .brand-name {
    font-family: "Michroma", sans-serif;
    color: var(--gold);
    letter-spacing: 4px;
    white-space: nowrap;
  }
  .brand-band .brand-name {
    position: absolute; left: 0; right: 0; top: 28px;
    text-align: center; font-size: 44px; line-height: 52px;
  }
  .front-url {
    position: absolute; left: 0; right: 0; top: 522px;
    text-align: center;
    font-family: "Exo 2", sans-serif; font-style: italic;
    font-size: 22px; letter-spacing: 7px;
    color: var(--text-soft);
  }

  /* Back */
  .rule { position: absolute; background: var(--rule); }
  .rule--v1 { left: 60px; top: 0; width: 4px; height: 580px; }
  .rule--v2 { left: 78px; top: 0; width: 3px; height: 580px; }
  .rule--h1 { left: 0; top: 503px; width: 1046px; height: 4px; }
  .rule--h2 { left: 0; top: 525px; width: 1046px; height: 3px; }

  .card--back .brand-name {
    position: absolute; left: 150px; top: 118px;
    font-size: 40px; line-height: 48px;
  }
  .holder-name {
    position: absolute; left: 148px; top: 186px;
    font-family: "Questrial", sans-serif;
    font-size: 35px; color: var(--text);
  }
  .contact {
    position: absolute;
    font-family: "Open Sans", sans-serif;
    font-size: 23px; line-height: 30px; color: var(--text);
  }
  .contact svg { position: absolute; fill: var(--text); }
  .contact--address { left: 218px; top: 370px; }
  .contact--address svg { left: -72px; top: 22px; width: 42px; height: 40px; }
  .contact--phone { left: 214px; top: 450px; }
  .contact--phone svg { left: -70px; top: -6px; width: 40px; height: 42px; }
  .contact--web { left: 701px; top: 383px; }
  .contact--web svg { left: -74px; top: -4px; width: 42px; height: 42px; }
  .contact--mail { left: 701px; top: 450px; }
  .contact--mail svg { left: -74px; top: 2px; width: 40px; height: 28px; }
</style>
</head>
<body>
<main class="sheet">

  <section class="card card--front" aria-label="Card front">
    <div class="brand-band">
      <div class="brand-name">GLEAMWISE</div>
    </div>
    <p class="front-url">www.gleamwise-gleamwise.com</p>
  </section>

  <section class="card card--back" aria-label="Card back">
    <span class="rule rule--v1"></span>
    <span class="rule rule--v2"></span>
    <span class="rule rule--h1"></span>
    <span class="rule rule--h2"></span>

    <div class="brand-name">GLEAMWISE</div>
    <h1 class="holder-name">Paul Dremmick</h1>

    <p class="contact contact--address">
      <svg viewBox="0 0 42 40" aria-hidden="true"><path d="M21 2 L40 19 L35 19 L35 38 L25 38 L25 26 L17 26 L17 38 L7 38 L7 19 L2 19 Z"/></svg>
      418 Harbor Lane<br>Fairview,OR 97024
    </p>

    <p class="contact contact--phone">
      <svg viewBox="0 0 40 42" aria-hidden="true"><g transform="rotate(-35 20 21)"><rect x="12" y="4" width="16" height="34" rx="3"/><rect x="15" y="8" width="10" height="10" fill="#2e3033"/><circle cx="17" cy="23" r="1.4" fill="#2e3033"/><circle cx="23" cy="23" r="1.4" fill="#2e3033"/><circle cx="17" cy="28" r="1.4" fill="#2e3033"/><circle cx="23" cy="28" r="1.4" fill="#2e3033"/><circle cx="17" cy="33" r="1.4" fill="#2e3033"/><circle cx="23" cy="33" r="1.4" fill="#2e3033"/></g></svg>
      +(555)01234567
    </p>

    <p class="contact contact--web">
      <svg viewBox="0 0 42 42" aria-hidden="true"><circle cx="21" cy="21" r="19"/><g fill="none" stroke="#2e3033" stroke-width="2.2"><ellipse cx="21" cy="21" rx="8" ry="17"/><line x1="4" y1="21" x2="38" y2="21"/><line x1="21" y1="4" x2="21" y2="38"/><path d="M7 12 H35 M7 30 H35"/></g></svg>
      www.companyname.com
    </p>

    <p class="contact contact--mail">
      <svg viewBox="0 0 40 28" aria-hidden="true"><rect x="0" y="0" width="40" height="28"/><path d="M2 2 L20 16 L38 2 M2 26 L15 13 M38 26 L25 13" fill="none" stroke="#2e3033" stroke-width="2.4"/></svg>
      contact@company name
    </p>
  </section>

</main>
</body>
</html>
```